Local Flower Farm Needs Business Card Design

I need business cards designed for a flower farm based in Eudora, Kansas.
Business Info:
We are a local cut flower farm located in Eudora, Kansas, founded by Darla Hoffstrom. What started as a passion for agriculture and search for more joy in daily life has blossomed into a small business dedicated to providing the community with beautiful, fresh, and sustainable flowers. We specialize in local, seasonal blooms, ensuring that every petal reflects the care and dedication we pour into our craft. Our mission is to deliver the highest quality flowers directly to our customers through local farmers markets and to florists who share our commitment to sustainability. Join us in celebrating the beauty of nature, one bloom at a time!
Contact Details:
Darla Hoffstrom
Owner
Phone 913-555-0147
Facebook: Lorabelle Quinn Blossoms
Instagram: @LorabelleQuinnBlossoms
Website: LorabelleQuinnBlossoms.example
Target Market(s)
Wholesale to Florists and Direct to Consumer via Farmers Market
Industry/Entity Type
Florist, Farm
Contact Information for Business Card
Name, Contact Info, Logo
Look and feel

```html
<!DOCTYPE html>
<html lang="en">
<head>
<meta charset="utf-8">
<title>Lorabelle Quinn Blossoms – Business Card</title>
<link rel="stylesheet" href="https://fonts.googleapis.com/css2?family=Montserrat:wght@400;500;600;700&display=swap">
<style>
  :root {
    --teal-dark: #0d2a30;
    --paper: #ffffff;
    --ink: #0d2a30;
    --stage: #333538;
  }
  * { margin: 0; padding: 0; box-sizing: border-box; }
  html, body { width: 1200px; height: 900px; overflow: hidden; }
  body {
    background: var(--stage);
    font-family: "Montserrat", sans-serif;
    position: relative;
  }
  .card {
    position: absolute;
    width: 620px;
    height: 354px;
    border-radius: 26px;
    overflow: hidden;
  }
  .card--back { left: 150px; top: 50px; background: var(--teal-dark); }
  .card--front { left: 430px; top: 480px; background: var(--paper); }

  .brand-seal {
    position: absolute;
    border-radius: 50%;
    display: flex;
    align-items: center;
    justify-content: center;
    text-align: center;
    font-weight: 500;
    text-transform: uppercase;
    line-height: 1.35;
  }
  .card--back .brand-seal {
    width: 210px; height: 210px;
    left: 205px; top: 72px;
    border: 1.5px solid var(--paper);
    color: var(--paper);
    font-size: 19px;
    letter-spacing: 2px;
  }
  .card--front .brand-seal {
    width: 132px; height: 132px;
    left: 40px; top: 30px;
    border: 1.2px solid var(--ink);
    color: var(--ink);
    font-size: 12px;
    letter-spacing: 1.4px;
  }

  .identity {
    position: absolute;
    right: 40px; top: 58px;
    width: 300px;
    color: var(--ink);
    text-align: center;
  }
  .identity__name {
    font-size: 30px;
    font-weight: 700;
    letter-spacing: 0.2px;
    padding-bottom: 6px;
    border-bottom: 2px solid var(--ink);
  }
  .identity__role {
    display: flex;
    align-items: center;
    gap: 10px;
    margin-top: 4px;
    font-size: 16px;
    font-weight: 500;
  }
  .identity__role::before, .identity__role::after {
    content: ""; flex: 1; height: 2px; background: var(--ink);
  }

  .contact-list {
    position: absolute;
    left: 120px; top: 176px;
    list-style: none;
    color: var(--ink);
    font-size: 15px;
    z-index: 1;
  }
  .contact-list li {
    display: flex; align-items: center; gap: 12px;
    height: 25px;
  }
  .contact-list svg { width: 17px; height: 17px; flex: none; }

  .front-band { position: absolute; left: 0; top: 0; width: 620px; height: 354px; }
</style>
</head>
<body>

  <section class="card card--back">
    <div class="brand-seal">Lorabelle<br>Quinn<br>Blossoms</div>
  </section>

  <section class="card card--front">
    <svg class="front-band" viewBox="0 0 620 354" aria-hidden="true">
      <path d="M0 326 L480 300 C515 298 515 222 555 222 H620 V354 H0 Z" fill="var(--teal-dark)"/>
      <path d="M0 338 L490 312 C520 310 540 304 620 302" fill="none" stroke="var(--paper)" stroke-width="5"/>
    </svg>

    <div class="brand-seal">Lorabelle<br>Quinn<br>Blossoms</div>

    <div class="identity">
      <div class="identity__name">Darla Hoffstrom</div>
      <div class="identity__role">Owner</div>
    </div>

    <ul class="contact-list">
      <li>
        <svg viewBox="0 0 24 24"><path fill="var(--ink)" d="M6.6 10.8a15.1 15.1 0 0 0 6.6 6.6l2.2-2.2a1 1 0 0 1 1-.25 11.4 11.4 0 0 0 3.6.57 1 1 0 0 1 1 1V20a1 1 0 0 1-1 1A17 17 0 0 1 3 4a1 1 0 0 1 1-1h3.5a1 1 0 0 1 1 1c0 1.250.2 2.450.57 3.57a1 1 0 0 1-.25 1z"/></svg>
        913-555-0147
      </li>
      <li>
        <svg viewBox="0 0 24 24"><circle cx="12" cy="12" r="10" fill="var(--ink)"/></svg>
        Lorabelle Quinn Blossoms
      </li>
      <li>
        <svg viewBox="0 0 24 24"><rect x="2" y="2" width="20" height="20" rx="4" fill="var(--ink)"/></svg>
        @LorabelleQuinnBlossoms
      </li>
      <li>
        <svg viewBox="0 0 24 24"><g fill="none" stroke="var(--ink)" stroke-width="2"><circle cx="12" cy="12" r="10"/><ellipse cx="12" cy="12" rx="4.5" ry="10"/><path d="M2 12h20M4 7h16M4 17h16"/></g></svg>
        LorabelleQuinnBlossoms.example
      </li>
    </ul>
  </section>

</body>
</html>
```